Car rental website design for a UAE car rental company

This project is about creating a new website design for a car rental company located in Dubai (United Arab Emirates), I opened the same project a few months ago but I didn't receive a lot of appealing entries so I closed it but this time I am marking the project as guaranteed to avoid such situation again, if you have already provided a design before then please re-submit again on this project so that it is considered while reviewing all the designs

A few important things:

1- We need a simple non-complex design
2- The final deliverable would be 2 screens (PSD, JPEG ... etc), the first screen is for the home page and the second screen is for an internal page
3- The home page must have a section that end users can use to rent a car online directly from the home page instead of going into some inner pages
4- The current website is very old and not very appealing so avoid creating a similar design (www.quarvin-drive.example)
5- The name is Quarvin but the company rents normal cars (no Limousin cars will be rented) so avoid adding any fancy cars in the images/graphics used in the design, just normal end users cars
6- The expected pages would be: home, About us, Our team, Strategy, Contact us and links to social media pages
7- The attachments include the company's logo and some screens from other car rental companies that provide online rentals/payments

If you have any questions please feel free to ask and please note that we will need the designs urgently

Thanks

Target Market(s)

Dubai - United Arab Emirates

Industry/Entity Type

It Company

Number of Pages Required

2 page

Font styles to use
Sans Serif

Requirements
Must have
• Check the project details
Nice to have
Should not have

```html
<!DOCTYPE html>
<html lang="en">
<head>
<meta charset="utf-8">
<title>Quarvin – Rent A Car</title>
<link rel="stylesheet" href="https://fonts.googleapis.com/css2?family=Open+Sans:wght@300;400;600;700&display=swap">
<style>
:root{
  --crimson:#980a2b;
  --crimson-dark:#7d0823;
  --charcoal:#333333;
  --charcoal-deep:#2a2a2a;
  --orange:#f07d0a;
  --orange-light:#f89a1c;
  --cyan:#1aa3d4;
  --yellow:#f5c400;
  --red:#e0101a;
  --field-pink:#e8c5cc;
  --line:#dddddd;
  --text:#333333;
  --white:#ffffff;
  --brand-tan:#c9a9a0;
}
*{box-sizing:border-box;margin:0;padding:0}
html,body{width:1200px;height:2546px;overflow:hidden}
body{font-family:'Open Sans',sans-serif;color:var(--text);background:var(--white);position:relative}
.abs{position:absolute}

/* header */
.site-header{position:absolute;left:0;top:0;width:1200px;height:156px;background:var(--crimson)}
.top-strip{position:absolute;left:0;top:0;width:1200px;height:36px;background:var(--charcoal-deep)}
.account-links{position:absolute;left:806px;top:7px;color:var(--white);font-size:15px}
.social-mini{position:absolute;left:944px;top:9px;display:flex;gap:11px}
.social-mini span{width:18px;height:18px;border-radius:50%;background:var(--white);position:relative}
.social-mini span::after{content:"";position:absolute;left:6px;top:6px;width:6px;height:6px;border-radius:50%;background:var(--charcoal-deep)}
.brand{position:absolute;left:104px;top:52px;width:128px;text-align:center}
.brand-mark{width:44px;height:46px;margin:0 auto 4px;background:var(--white);border:3px solid #b9aaa4}
.brand-name{font-size:22px;font-weight:600;line-height:1;color:var(--brand-tan)}
.brand-tag{font-size:11px;font-weight:600;color:var(--white);letter-spacing:1px}
.main-nav{position:absolute;top:84px;left:521px;display:flex;align-items:center;font-size:14px;font-weight:600;color:var(--white)}
.main-nav a{color:inherit;text-decoration:none;padding:3px 0;margin-right:40px}
.main-nav a.active{background:linear-gradient(#ffffff,#dcdcdc);color:var(--crimson);padding:3px 18px;border-radius:3px;margin-right:24px}
.search-icon{position:absolute;left:1054px;top:80px}

/* hero */
.hero{position:absolute;left:0;top:156px;width:1200px;height:553px;background:var(--charcoal)}
.hero-photo{position:absolute;left:98px;top:51px;width:1003px;height:436px;
  background:
    radial-gradient(ellipse 230px 150px at 300px 250px,rgba(214,82,30,.95),rgba(214,82,30,0) 100%),
    radial-gradient(ellipse 420px 140px at 820px 200px,rgba(40,52,40,.85),rgba(40,52,40,0) 100%),
    linear-gradient(180deg,#c8cdcf 0%,#9aa4a6 30%,#5a6460 55%,#3a3e3e 75%,#24272a 100%);
  box-shadow:0 8px 18px rgba(0,0,0,.45)}
.hero-title{position:absolute;left:710px;top:236px;color:var(--white);font-size:40px;font-weight:600;line-height:1.18;text-shadow:0 2px 4px rgba(0,0,0,.35)}
.slide-arrow{position:absolute;top:244px;width:56px;height:45px;background:var(--crimson);display:flex;align-items:center;justify-content:center}
.slide-arrow.prev{left:76px}.slide-arrow.next{left:1069px}
.slide-dots{position:absolute;top:513px;left:562px;display:flex;gap:6px}
.slide-dots span{width:21px;height:21px;border-radius:50%;background:var(--white)}

/* booking */
.booking{position:absolute;left:0;top:709px;width:1200px;height:245px;background:var(--crimson)}
.grab-card{position:absolute;left:98px;top:14px;width:201px;height:136px;background:var(--orange)}
.grab-card::after{content:"";position:absolute;right:-20px;top:56px;border:11px solid transparent;border-left:10px solid var(--orange)}
.grab-text{position:absolute;left:84px;top:46px;color:var(--white)}
.grab-text strong{display:block;font-size:19px;font-weight:600;line-height:1.1}
.grab-text small{font-size:12px;font-weight:600}
.manage-card{position:absolute;left:98px;top:155px;width:201px;height:61px;background:#86928d;color:var(--white);font-size:11px;line-height:1.2;padding:17px 0 0 60px}
.manage-card::before{content:"";position:absolute;left:14px;top:12px;width:36px;height:36px;border:2px solid var(--white);border-radius:3px}
.field-label{position:absolute;color:var(--white);font-size:14px;font-weight:600}
.field{position:absolute;height:31px;background:linear-gradient(#ffffff,#e2e2e2);border-radius:3px}
.field.select::after{content:"";position:absolute;right:20px;top:4px;height:23px;border-left:1px solid #bbb}
.field.select::before{content:"▴\A▾";white-space:pre;position:absolute;right:6px;top:4px;font-size:10px;line-height:12px;color:#555}
.btn-quote,.btn-world{position:absolute;top:187px;height:29px;font-size:11px;font-weight:600;display:flex;align-items:center;justify-content:center}
.btn-quote{left:772px;width:160px;background:var(--cyan);color:var(--white)}
.btn-world{left:945px;width:156px;background:linear-gradient(var(--yellow),#f29a00);color:#333}

/* featured */
.section-bar{position:absolute;top:977px;height:43px;background:linear-gradient(#3a3a3a,#242424);color:var(--white);font-size:14px;font-weight:600;padding:12px 0 0 26px}
.section-bar::before{content:"";position:absolute;left:0;top:0;border-top:43px solid var(--red);border-right:16px solid transparent}
.car-card{position:absolute;top:1045px;width:233px;height:323px;border:1px solid var(--line);background:var(--white)}
.car-photo{position:absolute;left:8px;top:10px;width:215px;height:212px}
.car-caption{position:absolute;left:17px;top:235px;width:200px;color:var(--red);font-size:12px;line-height:1.4}
.car-price{position:absolute;left:17px;top:277px;font-size:16px;display:flex;gap:8px;align-items:center}
.car-price .old{background:var(--red);color:var(--white);padding:0 4px}
.makers{position:absolute;left:98px;top:1410px;width:1003px;height:97px;border:1px solid var(--line);display:flex}
.makers span{flex:1;border-right:1px solid var(--line);display:flex;align-items:center;justify-content:center;font-size:13px;font-weight:600;color:#6a6a6a}
.makers span:last-child{border-right:0}

/* testimonials */
.testimonials{position:absolute;left:0;top:1548px;width:1200px;height:488px;
  background:
    radial-gradient(ellipse 260px 200px at 900px 330px,rgba(120,124,130,.45),rgba(120,124,130,0)),
    radial-gradient(ellipse 380px 300px at 200px 200px,rgba(110,118,130,.55),rgba(110,118,130,0)),
    linear-gradient(100deg,#4a515c 0%,#363b44 50%,#25282e 100%);
  color:var(--white);text-align:center}
.testimonials h2{position:absolute;top:40px;width:100%;font-size:44px;font-weight:400}
.quote-mark{position:absolute;top:118px;width:100%;font-size:150px;font-weight:700;line-height:.8;height:80px;overflow:hidden;font-family:Georgia,serif}
.testimonials h3{position:absolute;top:212px;width:100%;font-size:25px;font-weight:400}
.testimonials p{position:absolute;left:108px;top:258px;width:984px;font-size:12.5px;line-height:1.4}
.btn-outline{position:absolute;left:545px;top:366px;width:108px;height:41px;border:2px solid var(--white);font-size:13px;display:flex;align-items:center;justify-content:center}

/* newsletter */
.newsletter{position:absolute;left:0;top:2036px;width:1200px;height:146px;background:var(--crimson)}
.newsletter h4{position:absolute;left:98px;top:54px;color:var(--white);font-size:26px;font-weight:400}
.news-input{position:absolute;top:50px;height:49px;background:var(--field-pink);border:2px solid #f3dde1;font-size:14px;font-style:italic;color:#555;padding:13px 14px}
.btn-submit{position:absolute;left:954px;top:50px;width:147px;height:49px;background:linear-gradient(var(--orange-light),var(--orange));color:var(--white);font-size:18px;font-weight:600;display:flex;align-items:center;justify-content:center}

/* contact */
.get-in-touch{position:absolute;left:0;top:2182px;width:1200px;height:258px;background:var(--charcoal);color:var(--white);text-align:center}
.get-in-touch h2{position:absolute;top:35px;width:100%;font-size:48px;font-weight:400}
.get-in-touch p{position:absolute;left:205px;top:107px;width:790px;font-size:17px;line-height:1.3}
.social-row{position:absolute;top:180px;left:472px;display:flex;gap:26px}
.social-row span{width:32px;height:32px;border-radius:50%;background:var(--white);position:relative}
.social-row span::after{content:"";position:absolute;left:11px;top:11px;width:10px;height:10px;border-radius:50%;background:var(--charcoal)}
.footer-links{position:absolute;left:0;top:2440px;width:1200px;height:46px;background:var(--crimson);color:var(--white);font-size:15px;text-align:center;padding-top:12px}
.footer-base{position:absolute;left:0;top:2486px;width:1200px;height:60px;background:var(--charcoal-deep);color:var(--white);font-size:14px;padding:18px 0 0 98px}
</style>
</head>
<body>

<header class="site-header">
  <div class="top-strip"></div>
  <div class="account-links">Sign up | Sign In</div>
  <div class="social-mini" aria-label="Social links"><span></span><span></span><span></span><span></span><span></span></div>
  <div class="brand">
    <div class="brand-mark"></div>
    <div class="brand-name">Quarvin</div>
    <div class="brand-tag">Rent A Car</div>
  </div>
  <nav class="main-nav">
    <a class="active">Home</a><a>About</a><a>Gallery</a><a>Services</a><a>News</a><a>Contact</a>
  </nav>
  <svg class="search-icon" width="34" height="34" viewBox="0 0 34 34"><circle cx="13" cy="13" r="9" fill="none" stroke="#fff" stroke-width="3"/><line x1="20" y1="20" x2="30" y2="30" stroke="#fff" stroke-width="4" stroke-linecap="round"/></svg>
</header>

<section class="hero">
  <div class="hero-photo" role="img" aria-label="Orange hatchback driving fast along a road under a cloudy sky with dark hills"></div>
  <div class="hero-title">Rent exclusive car<br>for your special<br>occasion!</div>
  <div class="slide-arrow prev"><svg width="16" height="22" viewBox="0 0 16 22"><polyline points="12,2 3,11 12,20" fill="none" stroke="#fff" stroke-width="3"/></svg></div>
  <div class="slide-arrow next"><svg width="16" height="22" viewBox="0 0 16 22"><polyline points="4,2 13,11 4,20" fill="none" stroke="#fff" stroke-width="3"/></svg></div>
  <div class="slide-dots"><span></span><span></span><span></span></div>
</section>

<section class="booking">
  <div class="grab-card">
    <svg class="abs" style="left:8px;top:40px" width="72" height="56" viewBox="0 0 72 56" fill="none" stroke="#fff" stroke-width="3"><path d="M4 30 L10 16 H34 L40 30 V42 H4 Z"/><circle cx="12" cy="42" r="4"/><circle cx="32" cy="42" r="4"/><path d="M30 18 L36 6 H58 L64 18 V30 H44"/><path d="M26 44 L32 32 H56 L62 44 V54 H26 Z" fill="#fff"/></svg>
    <div class="grab-text"><strong>Grab A Car</strong><small>In Few Seconds</small></div>
  </div>
  <div class="manage-card">View Change or Cancel<br>A Car Reservation</div>

  <div class="field-label" style="left:356px;top:12px">Pick up Location</div>
  <div class="field select" style="left:356px;top:31px;width:330px"></div>
  <div class="field-label" style="left:772px;top:12px">Return Location</div>
  <div class="field select" style="left:772px;top:31px;width:329px"></div>

  <div class="field-label" style="left:356px;top:90px">Pick-up Date &amp; Time *</div>
  <div class="field" style="left:356px;top:109px;width:167px"></div>
  <div class="field select" style="left:529px;top:109px;width:73px"></div>
  <div class="field select" style="left:611px;top:109px;width:75px"></div>
  <div class="field-label" style="left:772px;top:90px">Pick-up Date &amp; Time *</div>
  <div class="field" style="left:772px;top:109px;width:166px"></div>
  <div class="field select" style="left:945px;top:109px;width:73px"></div>
  <div class="field select" style="left:1027px;top:109px;width:74px"></div>

  <div class="field-label" style="left:356px;top:167px">Pick-up Date &amp; Time *</div>
  <div class="field select" style="left:356px;top:187px;width:330px"></div>
  <div class="btn-quote">GET A QUOTE</div>
  <div class="btn-world">Worldwide Booking</div>
</section>

<div class="section-bar" style="left:98px;width:747px">FEATURED CARS</div>
<div class="section-bar" style="left:871px;width:230px">SPECIALS</div>

<article class="car-card" style="left:98px">
  <div class="car-photo" role="img" aria-label="White sports coupe by the sea" style="background:radial-gradient(ellipse 110px 45px at 110px 140px,#f2f2f2,rgba(242,242,242,0)),linear-gradient(180deg,#8e9aa4 0%,#b8c2c8 40%,#7d868c 62%,#4c5358 100%)"></div>
  <div class="car-caption">Consectetur adipisicing elit</div>
  <div class="car-price"><span class="old">$25,000</span>$23,750</div>
</article>
<article class="car-card" style="left:356px">
  <div class="car-photo" role="img" aria-label="Red hatchback parked on a street" style="background:radial-gradient(ellipse 110px 55px at 100px 130px,#d8481e,rgba(216,72,30,0)),linear-gradient(180deg,#3e4a52 0%,#6a747a 40%,#4a4f55 70%,#2e3236 100%)"></div>
  <div class="car-caption">Mollitia quae laboriosam<br>corporis delectus</div>
  <div class="car-price">$38,999</div>
</article>
<article class="car-card" style="left:613px">
  <div class="car-photo" role="img" aria-label="Silver crossover on a road" style="background:radial-gradient(ellipse 115px 50px at 110px 130px,#e2e5e7,rgba(226,229,231,0)),linear-gradient(180deg,#2f4450 0%,#55666e 40%,#6c7276 65%,#3a3e42 100%)"></div>
  <div class="car-caption">Non magni autem repellendus</div>
  <div class="car-price"><span class="old">$70,500</span>$64,860</div>
</article>
<article class="car-card" style="left:871px">
  <div class="car-photo" role="img" aria-label="Black hatchback in a bright studio" style="background:radial-gradient(ellipse 110px 50px at 120px 135px,#1e2124,rgba(30,33,36,0)),linear-gradient(180deg,#aab4bc 0%,#c7cfd5 45%,#9aa2a8 75%,#7f878d 100%)"></div>
  <div class="car-caption">Exercitationem voluptate<br>beatae</div>
  <div class="car-price"><span class="old">$70,500</span>$66,975</div>
</article>

<div class="makers">
  <span>Norvale</span><span>Kestrel</span><span>Ardent</span><span>Calloway</span><span>Dunmore</span>
  <span>Fenwa</span><span>Fielder</span><span>Hanari</span><span>Hyveron</span><span>Izmera</span>
</div>

<section class="testimonials" role="img" aria-label="Hand handing over car keys beside a car, darkened">
  <h2>TESTIMONIALS</h2>
  <div class="quote-mark">“</div>
  <h3>EU FUGIAT NULLA PARIATUR</h3>
  <p>Lorem ipsum dolor sit amet conse ctetur adipisicing elit, sed do eiusmod tempor incididunt ut labore et dolore magna aliqua. Ut enim ad minim veniam, quis nostrud exercitation ullamco laboris nisi ut aliquip ex ea commodo consequat. Duis aute irure dolor in reprehenderit in voluptate velit esse cillum dolore eu fugiat nulla pariatur.<br>Excepteur sint occaecat cupidatat non proident,.</p>
  <div class="btn-outline">SEE ALL</div>
</section>

<section class="newsletter">
  <h4>Signup For Newsletter:</h4>
  <div class="news-input" style="left:400px;width:264px">Email...</div>
  <div class="news-input" style="left:675px;width:263px">Phone Number...</div>
  <div class="btn-submit">Submit</div>
</section>

<section class="get-in-touch">
  <h2>Get In Touch</h2>
  <p>Lorem ipsum dolor sit amet, consectetur adipisicing elit, sed do eiusmod tempor incididunt ut<br>et dolore magna aliqua. Ut enim ad minim veniam, quis nostrud.</p>
  <div class="social-row" aria-label="Social links"><span></span><span></span><span></span><span></span><span></span></div>
</section>

<nav class="footer-links">About &nbsp;|&nbsp; Services &nbsp;|&nbsp; Downloads &nbsp;|&nbsp; Customer Support &nbsp;|&nbsp; Contact &nbsp;|&nbsp; Career &nbsp;|&nbsp; FAQs</nav>
<footer class="footer-base">Copyright 2014 All Rtight Reserved</footer>

</body>
</html>
```